Cosmetic injections clinic needs a fresh looking business card

We need a business card using the supplied logo and color scheme to attract future clients to our clinic. It should be modern and fresh, eye catching and not too busy. Simple and to the point is best. I would like two sided designs with the front indicating address and contact information, and the back in full color with white logo and descriptive information also provided.
Target Market(s)
Clients looking for non surgical beauty enhancements.
Contact Information for Business Card
MeloraSkin
14, 618 Birchmont Way
St. Albert, Alberta
K2P 7W3
Phone: 587-412-6630
Email: info@meloraskin.com
Requirements
Must have
- -Logo supplied with the name and address of the clinic
- -Back of card in full color with white logo with A small line of text indicating both of the following: Anti aging consultants and cosmetic injectables
- Located inside the Voyager Wellness Group

```html
<!DOCTYPE html>
<html lang="en">
<head>
<meta charset="utf-8">
<title>MeloraSkin Business Card</title>
<link rel="stylesheet" href="https://fonts.googleapis.com/css2?family=Open+Sans:wght@400;600;700&display=swap">
<style>
  :root {
    --pink: #e2479a;
    --teal: #26b8a3;
    --purple: #6c449c;
    --white: #ffffff;
    --trim: #111111;
  }
  * { box-sizing: border-box; margin: 0; padding: 0; }
  html, body {
    width: 913px;
    height: 1200px;
    overflow: hidden;
    background: var(--white);
    font-family: "Open Sans", sans-serif;
  }
  .sheet { position: relative; width: 913px; height: 1200px; }

  /* Back of card (full colour) */
  .card-back {
    position: absolute;
    left: 8px; top: 0;
    width: 905px; height: 606px;
    background: var(--pink);
  }
  .card-back .trim {
    position: absolute;
    left: 30px; top: 29px;
    width: 846px; height: 547px;
    border: 2px solid var(--trim);
  }
  .brand-mark {
    position: absolute;
    display: flex;
    align-items: center;
    gap: 20px;
  }
  .brand-mark--white { left: 0; right: 0; top: 190px; justify-content: center; }
  .brand-mark--white .brand-dot {
    width: 72px; height: 72px; border-radius: 50%;
    background: var(--white);
  }
  .brand-mark--white .brand-name {
    color: var(--white);
    font-size: 84px;
    font-weight: 600;
    line-height: 1;
  }
  .card-back .tagline {
    position: absolute;
    left: 124px; top: 474px;
    color: var(--white);
    font-size: 28.5px;
    font-weight: 400;
    white-space: nowrap;
  }

  /* Front of card (contact) */
  .card-front {
    position: absolute;
    left: 20px; top: 606px;
    width: 893px; height: 594px;
    background: var(--white);
  }
  .card-front .contact-panel {
    position: absolute;
    left: 0; top: 0;
    width: 471px; height: 594px;
    background: var(--teal);
  }
  .card-front .trim {
    position: absolute;
    left: 28px; top: 17px;
    width: 846px; height: 547px;
    border: 2px solid var(--trim);
  }
  .contact {
    position: absolute;
    left: 75px; top: 334px;
    color: var(--white);
    font-size: 31px;
    font-weight: 400;
    line-height: 37px;
    list-style: none;
    white-space: nowrap;
  }
  .brand-mark--colour { right: 67px; top: 120px; }
  .brand-mark--colour .brand-dot {
    width: 46px; height: 46px; border-radius: 50%;
    background: var(--purple);
  }
  .brand-mark--colour .brand-name {
    color: var(--purple);
    font-size: 54px;
    font-weight: 600;
    line-height: 1;
  }
  .services {
    position: absolute;
    right: 69px; top: 306px;
    color: var(--teal);
    font-size: 30px;
    font-weight: 700;
    line-height: 38.5px;
    text-align: right;
    text-transform: uppercase;
  }
</style>
</head>
<body>
<main class="sheet">
  <section class="card-back" aria-label="Back of card">
    <div class="trim"></div>
    <div class="brand-mark brand-mark--white">
      <span class="brand-dot"></span>
      <span class="brand-name">MeloraSkin</span>
    </div>
    <p class="tagline">Anti aging consultants and cosmetic injectables</p>
  </section>

  <section class="card-front" aria-label="Front of card">
    <div class="contact-panel"></div>
    <div class="trim"></div>
    <ul class="contact">
      <li>MeloraSkin</li>
      <li>14, 618 Birchmont Way</li>
      <li>St. Albert, Alberta K2P 7W3</li>
      <li>t: 587-412-6630</li>
      <li>e: info@meloraskin.com</li>
    </ul>
    <div class="brand-mark brand-mark--colour">
      <span class="brand-dot"></span>
      <span class="brand-name">MeloraSkin</span>
    </div>
    <p class="services">Anti aging<br>consultants<br>and<br>cosmetic<br>injectables</p>
  </section>
</main>
</body>
</html>
```